Life insurance company website and landing page

Web design is required for life insurance company. Specifically the company will 1) generate leads and 2) provide a blog. The target market of this business is people in their 50s and 60s, medium-high to high income earners, who are likely to have a policy in place already but want to save money on their premiums. Please read the attached design brief for more guidance. Open to any concepts that might work.The outputs for this job will include:1) a website2) a landing page3) fixing logos into a more useful and professional format (this should take 5 mins with the correct software)
Colors
Designer to choose colors to be used in the design.
Look and feel
Each slider illustrates characteristics of the customer's brand and the style your logo design should communicate.

```html
<!DOCTYPE html>
<html lang="en">
<head>
<meta charset="utf-8">
<title>CoverCompare.Life — Compare life insurance quotes</title>
<link href="https://fonts.googleapis.com/css2?family=Poppins:wght@500;600;700&family=Roboto:wght@400;500;700&display=swap" rel="stylesheet">
<style>
:root{
  --red:#e3131b;
  --ink:#1b1b1b;
  --text:#3a3a3a;
  --muted:#666;
  --rule:#555;
  --white:#fff;
  --blush:#f3f0f0;
  --grey-band:#dcdcdc;
  --charcoal:#2b2b2b;
  --footer:#262626;
  --box-line:#cfcfcf;
}
*{box-sizing:border-box;margin:0;padding:0}
html,body{width:1200px;height:3729px;overflow:hidden}
body{position:relative;font-family:"Roboto",Arial,sans-serif;color:var(--text);background:var(--white)}
.abs{position:absolute}
h1,h2,h3{font-family:"Poppins",Arial,sans-serif;color:var(--ink)}
.btn{position:absolute;display:flex;align-items:center;justify-content:center;background:var(--red);color:var(--white);font-family:"Poppins",Arial,sans-serif;font-weight:700;text-transform:uppercase;text-decoration:none}

/* header */
.site-header{position:absolute;left:0;top:0;width:1200px;height:116px;background:var(--white)}
.brand{position:absolute;display:flex;align-items:center;gap:14px;font-family:"Roboto",Arial,sans-serif;font-weight:400;color:var(--ink)}
.brand-dot{width:40px;height:40px;border-radius:50%;background:var(--red)}
.header-brand{left:132px;top:26px;font-size:33px}
.contact{position:absolute;top:22px;display:flex;gap:10px;align-items:flex-start}
.contact small{display:block;font-size:12px;font-weight:700;color:var(--ink);letter-spacing:.3px}
.contact span{font-size:16px;color:var(--ink)}
.contact .phone-num{font-size:20px;font-weight:700;color:var(--red)}
.main-nav{position:absolute;top:80px;left:554px;display:flex;gap:0;font-size:14px;font-weight:500;color:var(--ink)}
.main-nav a{color:inherit;text-decoration:none;margin-right:24px}
.main-nav a.active{color:var(--red);text-decoration:underline;text-underline-offset:4px}

/* hero */
.hero{position:absolute;left:0;top:116px;width:1200px;height:564px;overflow:hidden}
.hero-photo{position:absolute;inset:0;background:linear-gradient(100deg,#f3e6b8 0%,#e7c76a 30%,#d8a23a 55%,#c2862a 75%,#9b6a28 100%)}
.hero-title{position:absolute;left:127px;top:110px;font-size:35px;line-height:44px;font-weight:600;color:var(--ink)}
.hero .btn{left:132px;top:272px;width:242px;height:46px;font-size:16px}
.slider-dots{position:absolute;left:545px;top:478px;display:flex;gap:17px}
.slider-dots i{width:9px;height:9px;border-radius:50%;background:#333;display:block}
.slider-dots i.on{background:var(--red)}
.hero-curve{position:absolute;left:0;bottom:0;width:1200px;height:120px}

/* intro */
.intro-photo{position:absolute;left:130px;top:718px;width:466px;height:462px;background:linear-gradient(135deg,#d9d4cc,#8e8a84 50%,#4a4745)}
.intro-rule{position:absolute;left:563px;top:788px;width:100px;height:3px;background:var(--rule)}
.intro-title{position:absolute;left:640px;top:823px;font-size:28px;line-height:37px;font-weight:700}
.intro-text{position:absolute;left:640px;top:926px;width:370px;font-size:17px;line-height:25.5px;color:var(--text)}
.intro .btn{left:643px;top:1060px;width:242px;height:49px;font-size:16px}

/* feature band */
.feature-band{position:absolute;left:0;top:1143px;width:1200px;height:551px}
.feature-bg{position:absolute;inset:0;width:1200px;height:551px}
.feature-copy{position:absolute;left:0;top:1334px;width:1200px;text-align:center;color:var(--white)}
.feature-copy h2{color:var(--white);font-size:27px;font-weight:700}
.feature-copy p{font-size:23px;line-height:33px;margin-top:12px;font-weight:400}
.feature-band-btn{left:525px;top:1489px;width:150px;height:48px;font-size:16px}

/* section heads */
.section-head{position:absolute;left:0;width:1200px;text-align:center}
.section-head h2{font-size:27px;font-weight:700}
.section-head p{font-size:17px;margin-top:10px;color:var(--text)}
.section-head .rule{display:block;width:52px;height:3px;background:var(--rule);margin:14px auto 0}

/* partners */
.partners{position:absolute;left:0;top:1617px;width:1200px;height:333px;background:var(--blush)}
.partner-badge{position:absolute;top:1799px;width:171px;height:94px;background:var(--white);box-shadow:0 3px 8px rgba(0,0,0,.12);display:flex;align-items:center;justify-content:center}
.partner-badge i{display:block;width:120px;height:30px;border-radius:4px;background:#bdbdbd}

/* benefits */
.benefit{position:absolute;top:2139px;width:291px;height:286px;border:3px solid var(--box-line);background:var(--white);text-align:center;padding:93px 26px 0}
.benefit-icon{position:absolute;left:50%;top:-49px;margin-left:-56px;width:112px;height:112px;border-radius:50%;border:3px solid var(--red);background:var(--white);display:flex;align-items:center;justify-content:center}
.benefit h3{font-family:"Poppins",Arial,sans-serif;font-size:18px;line-height:26px;font-weight:500;color:var(--ink)}
.benefit p{font-size:15.5px;line-height:21.5px;margin-top:14px;color:var(--text)}

/* blog */
.blog{position:absolute;left:0;top:2484px;width:1200px;height:556px;background:var(--grey-band)}
.blog-card{position:absolute;top:2627px;width:303px;height:369px;background:var(--white)}
.blog-thumb{height:167px}
.blog-card h3{font-family:"Poppins",Arial,sans-serif;font-size:16px;line-height:20px;font-weight:500;color:var(--ink);margin:24px 28px 0}
.blog-card p{font-size:13.5px;line-height:19px;margin:14px 28px 0;color:var(--text)}
.blog-card .btn{position:relative;display:flex;margin:18px 0 0 28px;width:98px;height:30px;font-size:11px}
.carousel-arrow{position:absolute;width:48px;height:46px;background:var(--charcoal);display:flex;align-items:center;justify-content:center}

/* testimonials */
.testimonials{position:absolute;left:0;top:3040px;width:1200px;height:550px;background:linear-gradient(180deg,#2c2c2c,#1e1e1e)}
.testimonials .section-head h2{color:var(--white)}
.testimonials .section-head .rule{background:var(--white)}
.quote-card{position:absolute;top:3189px;width:291px;height:347px;border:2px solid #d8d8d8;padding:36px 38px 0;color:#e6e6e6}
.quote-mark{font-family:"Poppins",Arial,sans-serif;font-size:60px;line-height:30px;font-weight:700;color:var(--white);height:34px}
.quote-date{font-size:12px;font-style:italic;margin-top:10px}
.quote-text{font-size:15px;line-height:21px;margin-top:14px}
.stars{color:var(--red);font-size:13px;letter-spacing:2px;margin-top:12px}
.quote-name{font-family:"Poppins",Arial,sans-serif;font-size:16.5px;font-weight:600;color:var(--white);margin-top:4px}
.quote-role{font-size:14.5px}
.quote-arrow{position:absolute;top:3336px}

/* footer */
.site-footer{position:absolute;left:0;top:3590px;width:1200px;height:139px;background:var(--footer)}
.footer-brand{left:133px;top:36px;font-size:33px;color:var(--white)}
.footer-links{position:absolute;right:129px;top:40px;font-size:14px;color:var(--white)}
.footer-copy{position:absolute;right:129px;top:74px;font-size:13px;color:#d5d5d5}
</style>
</head>
<body>

<header class="site-header">
  <div class="brand header-brand"><span class="brand-dot"></span>CoverCompare.Life</div>
  <div class="contact" style="left:636px">
    <svg width="34" height="26" viewBox="0 0 34 26" fill="none" stroke="#222" stroke-width="2"><rect x="1" y="1" width="32" height="24"/><path d="M1 1l16 13L33 1"/></svg>
    <div><small>E MAIL US</small><span>hello@covercompare.life</span></div>
  </div>
  <div class="contact" style="left:894px">
    <svg width="30" height="30" viewBox="0 0 24 24" fill="none" stroke="#222" stroke-width="1.6"><path d="M22 16.9v3a2 2 0 0 1-2.2 2 19.8 19.8 0 0 1-8.6-3.1 19.5 19.5 0 0 1-6-6A19.8 19.8 0 0 1 2.1 4.2 2 2 0 0 1 4.1 2h3a2 2 0 0 1 2 1.7c.1 1 .4 1.9.7 2.8a2 2 0 0 1-.5 2.1L8 9.8a16 16 0 0 0 6 6l1.3-1.3a2 2 0 0 1 2.1-.4c.9.3 1.8.6 2.8.7a2 2 0 0 1 1.7 2z"/><path d="M15 2a7 7 0 0 1 7 7M15 6a3 3 0 0 1 3 3"/></svg>
    <div><small>CALL US</small><span class="phone-num">555.010.2040</span></div>
  </div>
  <nav class="main-nav">
    <a class="active" href="#">HOME</a><a href="#">ABOUT US</a><a href="#">SERVICES</a><a href="#">BLOG</a><a href="#">TESTIMONIALS</a><a href="#">CONTACT US</a>
  </nav>
</header>

<section class="hero">
  <div class="hero-photo" role="img" aria-label="Smiling retired couple in cream knit cardigans embracing outdoors among autumn leaves"></div>
  <h1 class="hero-title">Compare quotes from<br>Australia's leading life<br>insurers for free today</h1>
  <a class="btn" href="#">Get free quotes now</a>
  <div class="slider-dots"><i></i><i></i><i class="on"></i><i></i><i></i></div>
  <svg class="hero-curve" viewBox="0 0 1200 120" preserveAspectRatio="none">
    <path d="M0 120V62C260 10 520 40 760 90C930 120 1080 70 1200 40V120Z" fill="#3a3a3a"/>
    <path d="M0 120V88C260 34 520 60 760 108C930 132 1080 92 1200 64V120Z" fill="#fff"/>
  </svg>
</section>

<section class="intro">
  <div class="intro-photo" role="img" aria-label="Insurance broker in a suit reviewing a policy document with a seated couple at a table"></div>
  <span class="intro-rule"></span>
  <h2 class="intro-title">Compare Australia’s leading<br>life insurers, free</h2>
  <p class="intro-text">CoverCompare.Life helps you find the most appropriate and cost effective options by comparing a variety of leading insurers at the same time</p>
  <a class="btn" href="#">Get free quotes now</a>
</section>

<section class="feature-band">
  <svg class="feature-bg" viewBox="0 0 1200 551" preserveAspectRatio="none">
    <defs>
      <linearGradient id="bandTone" x1="0" x2="1" y1="0" y2="1">
        <stop offset="0" stop-color="#3d3d3d"/><stop offset=".5" stop-color="#5a5550"/><stop offset="1" stop-color="#3a3836"/>
      </linearGradient>
    </defs>
    <path d="M0 0L137 96H1200V551L1071 474H0Z" fill="url(#bandTone)" role="img" aria-label="Dimmed photo of a mature couple relaxing together on a sofa"/>
  </svg>
</section>
<div class="feature-copy">
  <h2>Home of everything life insurance in Australia</h2>
  <p>Stay informed; everything you need to know about life<br>insurance and income protection in Australia</p>
</div>
<a class="btn feature-band-btn" href="#">Read more</a>

<section class="partners"></section>
<div class="section-head" style="top:1662px">
  <h2>Our Partners</h2>
  <p>Australia’s leading insurers, we can help you compare them</p>
  <span class="rule"></span>
</div>
<div class="partner-badge" style="left:130px"><i></i></div>
<div class="partner-badge" style="left:323px"><i></i></div>
<div class="partner-badge" style="left:516px"><i></i></div>
<div class="partner-badge" style="left:706px"><i></i></div>
<div class="partner-badge" style="left:898px"><i></i></div>

<div class="section-head" style="top:1993px">
  <h2>Key Benefits</h2>
  <span class="rule"></span>
</div>

<article class="benefit" style="left:127px">
  <div class="benefit-icon">
    <svg width="62" height="62" viewBox="0 0 62 62" fill="none" stroke="#e3131b" stroke-width="3"><circle cx="34" cy="15" r="11" fill="#e3131b" stroke="none"/><path d="M34 9v12M37 11h-4a2 2 0 0 0 0 4h2a2 2 0 0 1 0 4h-4" stroke="#fff" stroke-width="2"/><path d="M4 40l8-6h12l8 4h-10M10 52l8-6h12l18-10" /><path d="M8 36l10 16"/></svg>
  </div>
  <h3>Need a high level of<br>cover at a low price?</h3>
  <p>Our highly experienced brokers can help you compare 11 of Australia’s leading insurers simultaneously.</p>
</article>
<article class="benefit" style="left:456px">
  <div class="benefit-icon">
    <svg width="56" height="60" viewBox="0 0 56 60" fill="none" stroke="#e3131b" stroke-width="3"><path d="M8 4h26l10 10v20M8 4v50h24"/><path d="M14 18h22M14 26h22M14 34h16M14 42h12"/><rect x="34" y="40" width="18" height="16" fill="#e3131b"/><path d="M37 40v-5a6 6 0 0 1 12 0v5"/></svg>
  </div>
  <h3>No hidden fees</h3>
  <p>Pay the same as going direct to the insurer, or even less</p>
</article>
<article class="benefit" style="left:782px">
  <div class="benefit-icon">
    <svg width="64" height="60" viewBox="0 0 64 60" fill="none" stroke="#e3131b" stroke-width="3"><path d="M32 6l14 6v12c0 10-6 16-14 20-8-4-14-10-14-20V12z"/><circle cx="32" cy="20" r="4"/><path d="M26 32c2-4 10-4 12 0"/><path d="M4 28l6 18 10 8M60 28l-6 18-10 8"/></svg>
  </div>
  <h3>Learn how life<br>insurance works</h3>
  <p>For articles, videos, guides, and anything else life insurance related, visit our blog.</p>
</article>

<section class="blog"></section>
<div class="section-head" style="top:2526px">
  <h2>Latest Blog</h2>
  <span class="rule"></span>
</div>
<article class="blog-card" style="left:130px">
  <div class="blog-thumb" role="img" aria-label="Businesswoman and colleague working at a laptop in a bright office" style="background:linear-gradient(120deg,#e9eef3,#b9c3cc 60%,#6f7a86)"></div>
  <h3>Lorem Ipsum is simply<br>dummy text of the</h3>
  <p>Contrary to popular belief, Lorem Ipsum is not simply random text. It has roots in a piece.</p>
  <a class="btn" href="#">Read more</a>
</article>
<article class="blog-card" style="left:450px">
  <div class="blog-thumb" role="img" aria-label="Hand signing a contract on a dark desk" style="background:linear-gradient(120deg,#2a2f36,#4d5560 55%,#9aa2ab)"></div>
  <h3>Lorem Ipsum is simply<br>dummy text of the</h3>
  <p>Contrary to popular belief, Lorem Ipsum is not simply random text. It has roots in a piece.</p>
  <a class="btn" href="#">Read more</a>
</article>
<article class="blog-card" style="left:767px">
  <div class="blog-thumb" role="img" aria-label="Close view of hands writing notes on paperwork" style="background:linear-gradient(120deg,#d8d2c8,#a89e92 55%,#6e665e)"></div>
  <h3>Lorem Ipsum is simply<br>dummy text of the</h3>
  <p>Contrary to popular belief, Lorem Ipsum is not simply random text. It has roots in a piece.</p>
  <a class="btn" href="#">Read more</a>
</article>
<div class="carousel-arrow" style="left:0;top:2772px"><svg width="14" height="22" viewBox="0 0 14 22" fill="none" stroke="#fff" stroke-width="2.5"><path d="M12 2L3 11l9 9"/></svg></div>
<div class="carousel-arrow" style="left:1159px;top:2772px;width:41px"><svg width="14" height="22" viewBox="0 0 14 22" fill="none" stroke="#fff" stroke-width="2.5"><path d="M2 2l9 9-9 9"/></svg></div>

<section class="testimonials"></section>
<div class="section-head testimonials-head" style="top:3090px">
  <h2 style="color:#fff">Testimonials</h2>
  <span class="rule" style="background:#fff"></span>
</div>
<article class="quote-card" style="left:130px">
  <div class="quote-mark">“</div>
  <div class="quote-date">12 September 2019</div>
  <p class="quote-text">Sed ut perspiciatis unde omnis iste natus error sit voluptatem accusantium doloremque laudantium, totam rem ape riam, eaque ipsa quae ab illo inventore veritatis et quasi architecto beatae.</p>
  <div class="stars">★★★★★</div>
  <div class="quote-name">MARTIN</div>
  <div class="quote-role">Prospective Buyer</div>
</article>
<article class="quote-card" style="left:455px">
  <div class="quote-mark">“</div>
  <div class="quote-date">12 September 2019</div>
  <p class="quote-text">Sed ut perspiciatis unde omnis iste natus error sit voluptatem accusantium doloremque laudantium, totam rem ape riam, eaque ipsa quae ab illo inventore veritatis et quasi architecto beatae.</p>
  <div class="stars">★★★★★</div>
  <div class="quote-name">GRAHAM</div>
  <div class="quote-role">Prospective Buyer</div>
</article>
<article class="quote-card" style="left:780px">
  <div class="quote-mark">“</div>
  <div class="quote-date">12 September 2019</div>
  <p class="quote-text">Sed ut perspiciatis unde omnis iste natus error sit voluptatem accusantium doloremque laudantium, totam rem ape riam, eaque ipsa quae ab illo inventore veritatis et quasi architecto beatae.</p>
  <div class="stars">★★★★★</div>
  <div class="quote-name">COLIN VALE</div>
  <div class="quote-role">Prospective Buyer</div>
</article>
<svg class="quote-arrow" style="left:72px" width="16" height="28" viewBox="0 0 16 28" fill="none" stroke="#fff" stroke-width="3"><path d="M14 2L3 14l11 12"/></svg>
<svg class="quote-arrow" style="left:1110px" width="16" height="28" viewBox="0 0 16 28" fill="none" stroke="#fff" stroke-width="3"><path d="M2 2l11 12L2 26"/></svg>

<footer class="site-footer">
  <div class="brand footer-brand"><span class="brand-dot"></span>CoverCompare.Life</div>
  <div class="footer-links">Terms of Use &nbsp;| &nbsp;Contact Us &nbsp;| &nbsp;Privacy policy</div>
  <div class="footer-copy">Copyright © 2019 All Rights Reserved</div>
</footer>

</body>
</html>
```